Brightleaf Wellness Website Design

About The Client:
Brightleaf Wellness is a sugar-free foods chain store providing services to Diabetics. They focus on the China domestic market. They describe themselves as being the 3rd space for Diabetics, the space between hospital and the home that help improve the quality of life for people wit Diabetes (see attached infographics).

They regularly hold education and advice events throughout the China. Brightleaf Wellness distribute a wide product range of food that is suitable for diabetic people. Brightleaf Wellness operate as a Franchise, providing business development services and Industry knowledge. They are actively seeking business partnerships at present.

The Brief:
Design a Home page and secondary information page(PSD only no code) that communicates our company services and company philosophy(3rd Space).
The final design should communicate 'Health, Social Responsibility and Professionalism'.
Colour scheme should orientate around Blue and White, see attached logo.

Websites we like:

http://link.venomira.com/home/

https://www.paxtunel.com/

http://dev.zorvik.com/
Updates

Hello all, the client has advised us that he want to display the professional advice service available for diabetic people more so than a food distributor. The client is also hoping to use his website as a marketing platform to attract affiliates and build partnerships as part of Brightleaf Wellness's business expansion strategy.

So can you make the page more corporate, reliable and professional. Use images of experts/doctors interacting with patients and also training/knowledge transfer images.

Thanks

Hello all, could you include stock images of both Chinese and Caucasians

Yeaahhh, Infographics and photos have been uploaded. Feel free to use them in your designs and also as references.

Target Market(s)

The target market is Chinese B2B in the Diabetics industry and Entrepreneurs looking to cooperate with Brightleaf Wellness.

Industry/Entity Type

Education

Requirements
Must have
• menu navigation with 7-8 sections,
a full screen background image,
Social Media icons,
Logo in top left,
Site search.
Nice to have
• The website must be clear and easy to use, less complicated.

See attached files of some Brightleaf Wellness infographics. Feel free to include elements of these into the design.
Should not have
• Should not use stock images of people from any other country, the client wants stock images of Chinese people only. Avoid photos showing obesity.

```html
<!DOCTYPE html>
<html lang="en">
<head>
<meta charset="utf-8">
<title>Brightleaf Wellness</title>
<link rel="stylesheet" href="https://fonts.googleapis.com/css2?family=Source+Sans+3:wght@400;600&display=swap">
<style>
:root{
  --brand-blue:#1f6fb2;
  --nav-blue:#2a77b8;
  --nav-active:#1c5f99;
  --link-blue:#1b78bd;
  --accent-red:#cf1a1f;
  --text-grey:#555;
  --panel-grey:#ebebeb;
  --line-grey:#dcdcdc;
  --footer-dark:#4a4a4d;
  --white:#fff;
}
*{box-sizing:border-box;margin:0;padding:0}
html,body{width:1151px;height:1200px;overflow:hidden;background:var(--white)}
body{position:relative;font-family:"Source Sans 3",sans-serif;color:var(--text-grey)}
.abs{position:absolute}
.top-rule{left:0;top:0;width:1151px;height:3px;background:var(--brand-blue)}
.brand{left:186px;top:38px;display:flex;align-items:center;gap:8px}
.brand-mark{width:26px;height:26px;background:var(--brand-blue);border-radius:50%}
.brand-name{font-size:17px;font-weight:600;color:var(--brand-blue)}
.search{left:570px;top:39px;width:218px;height:22px;border:1px solid #cfcfcf;border-radius:3px;background:#f3f3f3;font-size:8px;color:#777;padding:6px 9px}
.search svg{position:absolute;right:7px;top:4px}
.lang-label{left:804px;top:43px;font-size:9px;color:#666}
.lang{left:882px;top:39px;width:95px;height:22px;border:1px solid #cfcfcf;border-radius:3px;background:#fafafa;font-size:9.5px;color:#444;padding:5px 0 0 30px}
.lang .flag{position:absolute;left:8px;top:6px;width:16px;height:10px;background:#2b4a8c}
.lang svg{position:absolute;right:7px;top:8px}
.nav{left:0;top:97px;width:1151px;height:37px;background:var(--nav-blue)}
.nav-home{left:173px;top:0;width:90px;height:37px;background:var(--nav-active)}
.nav-item{top:13px;transform:translateX(-50%);font-size:10px;color:var(--white);white-space:nowrap}
.hero{left:0;top:134px;width:1151px;height:393px;background:linear-gradient(100deg,#7a9e6a 0%,#c9b59a 30%,#d9bfa6 55%,#b8c9a8 80%,#7e9fbf 100%)}
.hero-arrow{width:60px;height:60px;border-radius:50%;background:rgba(160,160,170,.55);top:156px}
.hero-arrow svg{position:absolute;left:22px;top:17px}
.hero-caption{left:179px;top:293px;font-size:23px;line-height:33px;color:var(--white);text-shadow:0 1px 2px rgba(0,0,0,.35);font-weight:400}
.services{left:0;top:527px;width:1151px;height:227px;background:var(--panel-grey)}
.section-title{font-size:17px;color:var(--accent-red);text-transform:uppercase;font-weight:400;white-space:nowrap}
.center{transform:translateX(-50%);text-align:center}
.service{width:185px;transform:translateX(-50%);text-align:center;top:60px}
.service-icon{width:64px;height:64px;margin:0 auto;border-radius:50%;background:#f4f4f4;border:1px solid #d6d6d6;display:flex;align-items:center;justify-content:center}
.service-icon span{width:56px;height:56px;border-radius:50%;background:radial-gradient(circle at 50% 35%,#8a8a8a,#5e5e5e);display:flex;align-items:center;justify-content:center}
.service-icon.active span{background:radial-gradient(circle at 50% 35%,#4aa6e8,#1f74c0)}
.service h3{margin-top:16px;font-size:12.5px;font-weight:400;color:var(--link-blue)}
.service p{margin-top:9px;font-size:8.7px;line-height:14.8px;color:var(--text-grey)}
.about-text{left:186px;top:802px;width:780px;text-align:center;font-size:9.5px;line-height:16.5px}
.divider{left:173px;top:854px;width:805px;height:1px;background:var(--line-grey)}
.pager{font-size:12px;color:#999;letter-spacing:4px}
.product-box{width:166px;height:84px;border:1px solid #d8d8d8;top:912px;background:var(--white);padding:4px}
.product-box div{width:100%;height:100%;border-radius:2px}
.product-name{top:1010px;font-size:11.5px;color:var(--link-blue)}
.product-desc{top:1030px;width:166px;font-size:8.7px;line-height:15.5px}
.price{top:1074px;font-size:13px;color:var(--accent-red)}
.btn{width:73px;height:21px;border-radius:3px;background:linear-gradient(#5aa9e3,#2f82c8);color:var(--white);font-size:8px;text-align:center;line-height:21px;border:1px solid #2b74b3}
.tip-thumb{left:750px;width:65px;height:55px;border:1px solid #d8d8d8;padding:2px}
.tip-thumb div{width:100%;height:100%}
.tip-title{left:830px;font-size:11.5px;color:var(--link-blue)}
.tip-desc{left:830px;width:150px;font-size:8.5px;line-height:15px}
.tip-rule{left:750px;top:981px;width:228px;height:1px;background:var(--line-grey)}
.footer{left:0;top:1126px;width:1151px;height:74px;background:linear-gradient(#555558,var(--footer-dark))}
.footer-links{left:175px;top:21px;font-size:8px;color:var(--white);display:flex;gap:0;white-space:nowrap}
.footer-links span{padding:0 8px}
.footer-links span:first-child{padding-left:0}
.footer-links i{font-style:normal;color:#ddd}
.copyright{left:175px;top:43px;font-size:8px;color:var(--white)}
.follow{left:838px;top:32px;font-size:7.5px;color:var(--white)}
.social{top:23px;width:26px;height:26px;border-radius:50%}
</style>
</head>
<body>
<div class="abs top-rule"></div>

<header>
  <div class="abs brand"><span class="brand-mark"></span><span class="brand-name">Brightleaf Wellness</span></div>
  <div class="abs search">SEARCH :
    <svg width="11" height="11" viewBox="0 0 11 11"><circle cx="4.5" cy="4.5" r="3.5" fill="none" stroke="#bbb" stroke-width="1.2"/><line x1="7" y1="7" x2="10" y2="10" stroke="#bbb" stroke-width="1.2"/></svg>
  </div>
  <div class="abs lang-label">Select Language :</div>
  <div class="abs lang"><span class="flag"></span>English
    <svg width="8" height="5" viewBox="0 0 8 5"><path d="M1 1l3 3 3-3" fill="none" stroke="#333" stroke-width="1.3"/></svg>
  </div>
</header>

<nav class="abs nav">
  <div class="abs nav-home"></div>
  <span class="abs nav-item" style="left:218px">HOME</span>
  <span class="abs nav-item" style="left:302px">ABOUT US</span>
  <span class="abs nav-item" style="left:393px">SERVICES</span>
  <span class="abs nav-item" style="left:485px">PRODUCTS</span>
  <span class="abs nav-item" style="left:567px">FAQ</span>
  <span class="abs nav-item" style="left:634px">TIPS</span>
  <span class="abs nav-item" style="left:723px">TESTIMONIALS</span>
  <span class="abs nav-item" style="left:824px">FEATURES</span>
  <span class="abs nav-item" style="left:922px">CONTACT US</span>
</nav>

<section class="abs hero" role="img" aria-label="Photo of a smiling multi-generation Chinese family sitting together outdoors">
  <div class="abs hero-arrow" style="left:110px"><svg width="14" height="26" viewBox="0 0 14 26"><path d="M12 1L2 13l10 12" fill="none" stroke="#fff" stroke-width="1.5"/></svg></div>
  <div class="abs hero-arrow" style="left:989px"><svg width="14" height="26" viewBox="0 0 14 26"><path d="M2 1l10 12L2 25" fill="none" stroke="#fff" stroke-width="1.5"/></svg></div>
  <h1 class="abs hero-caption">GROUP OF SUGAR FREE FOOD CHAIN<br>STORES IN CHINA PROVIDING SERVICES TO DIABETES.</h1>
</section>

<section class="abs services">
  <h2 class="abs section-title center" style="left:582px;top:21px">Our Services</h2>
  <div class="abs service" style="left:263px">
    <div class="service-icon active"><span>
      <svg width="30" height="30" viewBox="0 0 30 30"><path d="M6 13a9 9 0 0 1 16-5" fill="none" stroke="#fff" stroke-width="3"/><path d="M24 3v7h-7z" fill="#fff"/><path d="M24 17a9 9 0 0 1-16 5" fill="none" stroke="#fff" stroke-width="3"/><path d="M6 27v-7h7z" fill="#fff"/></svg>
    </span></div>
    <h3>SOCIAL COMMUNICATION</h3>
    <p>Lorem Ipsum is simply dummy text of the printing and typesetting industry. Lorem Ipsum has been the industry's standard...</p>
  </div>
  <div class="abs service" style="left:475px">
    <div class="service-icon"><span>
      <svg width="30" height="30" viewBox="0 0 30 30"><path d="M4 16h22a11 8 0 0 1-22 0z" fill="none" stroke="#fff" stroke-width="2"/><path d="M10 13c2-3-2-4 0-8M15 13c2-3-2-4 0-8M20 13c2-3-2-4 0-8" fill="none" stroke="#fff" stroke-width="1.5"/></svg>
    </span></div>
    <h3>FOOD ADVICE</h3>
    <p>Lorem Ipsum is simply dummy text of the printing and typesetting industry. Lorem Ipsum has been the industry's standard...</p>
  </div>
  <div class="abs service" style="left:678px">
    <div class="service-icon"><span>
      <svg width="30" height="30" viewBox="0 0 30 30"><path d="M11 5h8M13 5v8L6 24a2 2 0 0 0 2 3h14a2 2 0 0 0 2-3l-7-11V5" fill="none" stroke="#fff" stroke-width="2"/><circle cx="13" cy="21" r="1.5" fill="#fff"/><circle cx="18" cy="23" r="1" fill="#fff"/></svg>
    </span></div>
    <h3>CHECKUP PRODUCTS</h3>
    <p>Lorem Ipsum is simply dummy text of the printing and typesetting industry. Lorem Ipsum has been the industry's standard...</p>
  </div>
  <div class="abs service" style="left:889px">
    <div class="service-icon"><span>
      <svg width="30" height="30" viewBox="0 0 30 30"><rect x="5" y="13" width="5" height="12" fill="none" stroke="#fff" stroke-width="2"/><path d="M10 14l4-8c2 0 3 1 3 3l-1 4h7a2 2 0 0 1 2 2l-2 9a2 2 0 0 1-2 1H10" fill="none" stroke="#fff" stroke-width="2"/></svg>
    </span></div>
    <h3>FOOD ADVICE</h3>
    <p>Lorem Ipsum is simply dummy text of the printing and typesetting industry. Lorem Ipsum has been the industry's standard...</p>
  </div>
</section>

<section>
  <h2 class="abs section-title center" style="left:571px;top:771px">About Brightleaf Wellness</h2>
  <p class="abs about-text">Lorem Ipsum is simply dummy text of the printing and typesetting industry. Lorem Ipsum has been the industry's standard dummy text ever since the 1500s, when an unknown printer took a galley of type and scrambled it to make a type specimen book. It has survived not only five centuries, but also the leap into electronic typesetting, remaining essentially unchanged</p>
  <div class="abs divider"></div>
</section>

<section>
  <h2 class="abs section-title" style="left:174px;top:875px">Our Products</h2>
  <span class="abs pager" style="left:695px;top:881px">‹›</span>

  <div class="abs product-box" style="left:173px"><div role="img" aria-label="Photo of a sugar free pancake mix box" style="background:linear-gradient(90deg,#fff 25%,#c9a463 40%,#d9b27a 60%,#fff 75%)"></div></div>
  <div class="abs product-box" style="left:362px"><div role="img" aria-label="Photo of vitamin supplement bottles" style="background:linear-gradient(90deg,#fff 30%,#5a4636 42%,#e58a34 58%,#fff 70%)"></div></div>
  <div class="abs product-box" style="left:551px"><div role="img" aria-label="Photo of a pack of sugar free marshmallow treats" style="background:linear-gradient(90deg,#fff 5%,#f2e07a 20%,#f4e68c 80%,#fff 95%)"></div></div>

  <h3 class="abs product-name" style="left:173px;font-weight:400">SUGAR FREE FOOD</h3>
  <h3 class="abs product-name" style="left:362px;font-weight:400">SUGAR FREE FOOD</h3>
  <h3 class="abs product-name" style="left:551px;font-weight:400">SUGAR FREE FOOD</h3>
  <p class="abs product-desc" style="left:173px">Lorem Ipsum is simply dummy text of the printing and typesetting industry.</p>
  <p class="abs product-desc" style="left:362px">Lorem Ipsum is simply dummy text of the printing and typesetting industry.</p>
  <p class="abs product-desc" style="left:551px">Lorem Ipsum is simply dummy text of the printing and typesetting industry.</p>
  <span class="abs price" style="left:173px">$ 15.00</span>
  <span class="abs price" style="left:362px">$ 15.00</span>
  <span class="abs price" style="left:551px">$ 15.00</span>
  <span class="abs btn" style="left:266px;top:1071px">VIEW DETAILS</span>
  <span class="abs btn" style="left:455px;top:1071px">VIEW DETAILS</span>
  <span class="abs btn" style="left:644px;top:1071px">VIEW DETAILS</span>
</section>

<section>
  <h2 class="abs section-title" style="left:753px;top:875px">Tips for Diabetes</h2>
  <span class="abs pager" style="left:956px;top:881px">‹›</span>

  <div class="abs tip-thumb" style="top:912px"><div role="img" aria-label="Photo of a glucose meter beside fresh vegetables" style="background:linear-gradient(135deg,#8aa06a,#c9c1b8 50%,#c8402c)"></div></div>
  <h3 class="abs tip-title" style="top:914px;font-weight:400">SUGAR FREE FOOD</h3>
  <p class="abs tip-desc" style="top:935px">Lorem Ipsum is simply dummy text of the printing and typesetting.</p>
  <div class="abs tip-rule"></div>
  <div class="abs tip-thumb" style="top:995px"><div role="img" aria-label="Photo of a blood sugar test on a fingertip" style="background:linear-gradient(135deg,#e8d4c4,#d9b39a 50%,#6a8fb5)"></div></div>
  <h3 class="abs tip-title" style="top:997px;font-weight:400">SUGAR FREE FOOD</h3>
  <p class="abs tip-desc" style="top:1018px">Lorem Ipsum is simply dummy text of the printing and typesetting.</p>
  <span class="abs btn" style="left:904px;top:1071px">VIEW DETAILS</span>
</section>

<footer class="abs footer">
  <div class="abs footer-links">
    <span>HOME</span><i>|</i><span>ABOUT US</span><i>|</i><span>SERVICES</span><i>|</i><span>PRODUCTS</span><i>|</i><span>FAQ</span><i>|</i><span>TIPS</span><i>|</i><span>TESTIMONIALS</span><i>|</i><span>FEATURES</span><i>|</i><span>CONTACT US</span>
  </div>
  <div class="abs copyright">COPYRIGHTS ©2013 BRIGHTLEAF WELLNESS. ALL RIGHT RESERVED</div>
  <div class="abs follow">FOLLOW US :</div>
  <span class="abs social" style="left:889px;background:#2f63b0"></span>
  <span class="abs social" style="left:919px;background:#1f78b4"></span>
  <span class="abs social" style="left:950px;background:#3aa6e6"></span>
</footer>
</body>
</html>
```